Software Company Business Card

We are looking for a new design of our business card. The design will also be used in the rest of our branding and marketing materials as we want to keep it all uniform. We sell POS software to fine/luxury jewelers and also offer other business services as well to help the jeweler manage their business and need something more updated, technical and fresh, preferably more on the masculine side. We do not want any designs with gems in them but if possible would like to incorporate the circle and arrow in the logo into the design, but not a requirement if you can't make it work. I would like to see a variety of the mix. The colors need to remain our blue and orange and the logo can not change. The squiggly lines have been used as our corporate identity for over 20 years and its time to update. Our company name is PELK (Bright Ledger Counter Solutions).

Target Market(s)

High End Jewelers

Industry/Entity Type

Software

Contact Information for Business Card

Requirements
Must have
• Our logo and the colors must remain the same. Blue is #d95d39 and Orange is #0f5682.
Nice to have
• The circle and arrow incorporated but not a requirement.
Should not have
• Anything jewelry or gem related.

```html
<!DOCTYPE html>
<html lang="en">
<head>
<meta charset="utf-8">
<title>PELK Business Card</title>
<link href="https://fonts.googleapis.com/css2?family=Open+Sans:wght@400;600;700&display=swap" rel="stylesheet">
<style>
  :root {
    --brand-blue: #0f5682;
    --brand-orange: #d95d39;
    --paper: #f6f6f4;
    --ink: #3a3a3a;
    --muted: #6b6b6b;
    --rule: #c9c9c9;
    --stage: #2b2c2f;
  }
  * { box-sizing: border-box; margin: 0; padding: 0; }
  html, body { width: 1200px; height: 873px; overflow: hidden; }
  body {
    background: var(--stage);
    font-family: "Open Sans", Arial, sans-serif;
    position: relative;
  }
  .card {
    position: absolute;
    top: 281px;
    width: 540px;
    height: 310px;
    border-radius: 3px;
    overflow: hidden;
  }
  .card--front { left: 40px; background: var(--paper); }
  .card--back { left: 620px; background: var(--brand-blue); color: #fff; }

  /* front */
  .front-brand {
    position: absolute; left: 42px; top: 80px; width: 215px;
  }
  .brand-name {
    font-weight: 600; font-size: 46px; line-height: 1; letter-spacing: 6px;
    color: var(--brand-blue);
  }
  .brand-descriptor {
    margin-top: 10px; font-weight: 400; font-size: 11px; letter-spacing: 0.2px;
    color: var(--muted);
  }
  .divider {
    position: absolute; left: 272px; top: 48px; width: 1px; height: 150px;
    background: var(--rule);
  }
  .contact {
    position: absolute; left: 292px; top: 50px; width: 235px; color: var(--ink);
  }
  .contact__name {
    font-weight: 700; font-size: 18px; color: var(--brand-blue); line-height: 1.2;
  }
  .contact__role { font-size: 12px; margin-bottom: 12px; }
  .contact__list { list-style: none; font-size: 11.5px; line-height: 1.55; }
  .contact__list li { display: flex; align-items: center; gap: 7px; }
  .contact__list svg { width: 10px; height: 10px; flex: none; }
  .contact__label { color: var(--brand-orange); }
  .address-band {
    position: absolute; left: 0; bottom: 0; width: 100%; height: 44px;
    background: var(--brand-blue); display: flex; align-items: center;
  }
  .address-band__text {
    padding-left: 34px; color: #fff; font-size: 13px; letter-spacing: 0.2px; flex: 1;
  }
  .address-band__accent {
    width: 92px; height: 100%; background: var(--brand-orange);
  }

  /* back */
  .back-brand {
    position: absolute; left: 150px; top: 100px;
  }
  .back-brand .brand-name { color: #fff; font-size: 58px; letter-spacing: 8px; }
  .back-brand .brand-descriptor { color: #dbe6ee; font-size: 12px; }
  .back-url {
    position: absolute; left: 150px; top: 226px; font-size: 11px; letter-spacing: 1.5px;
    color: #dbe6ee;
  }
</style>
</head>
<body>
  <section class="card card--front" aria-label="Business card front">
    <div class="front-brand">
      <div class="brand-name">PELK</div>
      <div class="brand-descriptor">Bright Ledger Counter Solutions</div>
    </div>
    <div class="divider"></div>
    <div class="contact">
      <div class="contact__name">Rowan Ellery</div>
      <div class="contact__role">Founder</div>
      <ul class="contact__list">
        <li><svg viewBox="0 0 10 10"><path d="M2 1 L4 1 L5 3 L4 4 Q5 6 6 6 L7 5 L9 6 L9 8 Q5 9 2 5 Q1 3 2 1Z" fill="var(--brand-blue)"/></svg>1-800-555-0142 <span class="contact__label">(Toll Free)</span></li>
        <li><svg viewBox="0 0 10 10"><path d="M2 1 L4 1 L5 3 L4 4 Q5 6 6 6 L7 5 L9 6 L9 8 Q5 9 2 5 Q1 3 2 1Z" fill="var(--brand-blue)"/></svg>702-555-0187 <span class="contact__label">(Phone)</span></li>
        <li><svg viewBox="0 0 10 10"><rect x="1" y="2" width="8" height="6" fill="var(--brand-blue)"/><rect x="3" y="1" width="4" height="2" fill="var(--brand-blue)"/></svg>702-555-0163</li>
        <li><svg viewBox="0 0 10 10"><rect x="1" y="2" width="8" height="6" fill="var(--brand-blue)"/><path d="M1 2 L5 6 L9 2" stroke="#fff" fill="none"/></svg>info@pelkledger.com</li>
        <li><svg viewBox="0 0 10 10"><circle cx="5" cy="5" r="4" fill="none" stroke="var(--brand-blue)"/><path d="M1 5 H9 M5 1 Q2 5 5 9 M5 1 Q8 5 5 9" stroke="var(--brand-blue)" fill="none" stroke-width="0.8"/></svg>www.pelkledger.com</li>
      </ul>
    </div>
    <div class="address-band">
      <span class="address-band__text">P.O. Box 41820, Carson Vale, NV 89410 USA</span>
      <span class="address-band__accent"></span>
    </div>
  </section>

  <section class="card card--back" aria-label="Business card back">
    <div class="back-brand">
      <div class="brand-name">PELK</div>
      <div class="brand-descriptor">Bright Ledger Counter Solutions</div>
    </div>
    <div class="back-url">www.pelkledger.com</div>
  </section>
</body>
</html>
```